依頼詳細
<デザインイメージ>
・ラグジュアリー/高級なイメージ
・VIPのように扱われている
・希少な会に招待されている
記載項目
最低限記載項目:キャッチコピーや見出し/講演タイトル/日時/場所
※講演タイトル/日時/場所については、添付ファイルに記載しています。
※これを使って下さいという素材は特に決まっていません。
サイズ
A4
ページ数
片面
希望イメージ
• +5 0 +5
• シンプル
複雑
• 単色
カラフル
• 暗い
明るい
• 日常
高級
• 遊び心
厳粛
• 未来的
伝統的
• 女性的
男性的
希望する色
黄・オレンジ系、グレー系
納品ファイル
• 高解像度JPG (.jpg)
• イラストレーター形式 (.ai)
• フォトショップ形式 (.psd)
• PNG形式 (.png)
補足説明
依頼公開後の追記内容
<追記>

・講演の内容/テーマ
・講演のスケジュール
・会場について
・チケットの料金
・お申し込み方法
・お問い合わせ先

こちらについては
裏面に記載しております。

チラシ作品として非常に完成度が高かった事に加えて、内容も洗練されていたことが決め手となりました。

この度は、誠に多くのミルダー様にご提案をいただきましたことを、心から感謝いたします。皆様のご提案のクオリティがどれも高く選定にとても悩みました。

この度選定できなかったミルダー様にも、ご縁次第で、また直接ご依頼をさせていただきたいと思っておりますので、今後ともどうぞよろしくお願いいたします。

```html
<!DOCTYPE html>
<html lang="ja">
<head>
<meta charset="UTF-8">
<title>ビリオネアの授業 2018 The Next Step</title>
<link rel="stylesheet" href="https://fonts.googleapis.com/css2?family=Noto+Sans+JP:wght@700;900&family=Noto+Serif+JP:wght@500;700&family=Great+Vibes&family=Tinos:wght@400&display=swap">
<style>
  :root {
    --sky-top: #3f7fbf;
    --sky-mid: #a9cbe8;
    --haze: #f4f6f8;
    --stair-grey: #b9c0c7;
    --stair-dark: #8d959d;
    --title-blue: #1f5fae;
    --title-light: #5fa3e0;
    --ink-navy: #14233a;
    --ink-dark: #1d1d22;
    --map-blue: #3b6fa8;
    --map-ground: #e8ecef;
  }
  * { margin: 0; padding: 0; box-sizing: border-box; }
  html, body { width: 849px; height: 1200px; overflow: hidden; background: #fff; }
  .flyer {
    position: relative;
    width: 849px;
    height: 1200px;
    overflow: hidden;
    font-family: "Noto Serif JP", serif;
    color: var(--ink-dark);
  }
  .scene {
    position: absolute;
    inset: 0;
    background:
      radial-gradient(ellipse 260px 520px at 50% 52%, rgba(255,255,255,0.85), rgba(255,255,255,0) 70%),
      linear-gradient(180deg, var(--sky-top) 0%, var(--sky-mid) 28%, var(--haze) 52%, var(--stair-grey) 78%, var(--stair-dark) 100%);
  }
  .title {
    position: absolute;
    font-family: "Noto Sans JP", sans-serif;
    font-weight: 900;
    color: var(--title-blue);
    background: linear-gradient(180deg, var(--title-light), var(--title-blue) 60%);
    -webkit-background-clip: text;
    background-clip: text;
    -webkit-text-fill-color: transparent;
    filter: drop-shadow(0 0 3px #fff) drop-shadow(0 0 2px #fff);
    line-height: 1;
    white-space: nowrap;
  }
  .title-main { left: 34px; top: 16px; font-size: 130px; letter-spacing: -2px; }
  .title-sub { left: 34px; top: 166px; font-size: 118px; }
  .edition-year {
    position: absolute; left: 290px; top: 180px;
    font-family: "Great Vibes", cursive; font-size: 80px;
    color: var(--ink-navy); line-height: 1;
  }
  .edition-label {
    position: absolute; left: 318px; top: 266px;
    font-family: "Great Vibes", cursive; font-size: 34px;
    color: var(--ink-navy); line-height: 1;
  }
  .tour-label {
    position: absolute; left: 106px; top: 326px;
    font-family: "Noto Sans JP", sans-serif; font-weight: 700;
    font-size: 34px; letter-spacing: 2px; color: var(--ink-dark);
  }
  .headline {
    position: absolute; left: 0; top: 0;
    width: 849px; height: 1200px;
    pointer-events: none;
  }
  .lecture-title {
    font-family: "Tinos", serif; font-weight: 400; font-size: 160px;
    fill: var(--ink-navy);
  }
  .event-date { font-family: "Tinos", "Noto Serif JP", serif; fill: var(--ink-dark); }
  .event-date .small { font-family: "Noto Serif JP", serif; font-weight: 700; font-size: 40px; }
  .event-date .big { font-size: 140px; }
  .event-date .kanji { font-family: "Noto Serif JP", serif; font-weight: 700; font-size: 82px; }
  .event-time, .event-venue {
    position: absolute;
    font-family: "Noto Serif JP", serif; font-weight: 700;
    color: var(--ink-dark); white-space: nowrap; line-height: 1.2;
  }
  .event-time { top: 910px; left: 330px; font-size: 22px; }
  .event-venue { top: 944px; left: 282px; font-size: 24px; }
  .access-map {
    position: absolute; left: 40px; top: 1005px;
    width: 257px; height: 66px;
    background: linear-gradient(180deg, var(--map-ground), #cfd7de);
    border: 1px solid var(--map-blue);
  }
  .access-note {
    position: absolute; left: 311px; top: 1014px;
    font-family: "Noto Sans JP", sans-serif; font-weight: 700;
    font-size: 13px; line-height: 1.5; color: var(--ink-dark);
  }
</style>
</head>
<body>
  <main class="flyer">
    <div class="scene" role="img" aria-label="青空と雲の下、光に向かって続く白い階段を上るスーツ姿のビジネスマンの後ろ姿の写真"></div>

    <h1 class="title title-main">ビリオネアの</h1>
    <div class="title title-sub">授業</div>
    <div class="edition-year">2018</div>
    <div class="edition-label">Billionaire lessons</div>
    <div class="tour-label">来日公演</div>

    <svg class="headline" viewBox="0 0 849 1200" aria-label="The Next Step 2018年9月17日(月・祝)">
      <text class="lecture-title" x="34" y="792" textLength="781" lengthAdjust="spacingAndGlyphs">The Next Step</text>
      <text class="event-date" x="184" y="900" textLength="575" lengthAdjust="spacingAndGlyphs"><tspan class="small">2018年</tspan><tspan class="big">9</tspan><tspan class="kanji">月</tspan><tspan class="big">17</tspan><tspan class="kanji">日</tspan><tspan class="small">(月・祝)</tspan></text>
    </svg>

    <p class="event-time">13:00～19:30(開場12:00)</p>
    <p class="event-venue">会場：なにわ中央記念ホール</p>

    <div class="access-map" role="img" aria-label="会場周辺の簡易アクセスマップ"></div>
    <p class="access-note">水都橋駅 徒歩5分<br>地下鉄みなと線/川辺電鉄本線</p>
  </main>
</body>
</html>
```